Medical clinic VALORECLIN sales materials presentation folder

I am looking for a professional design to a sales/presentation folder for VALORECLIN medical clinic. I would like to get picture of doctor in a class design.
I had an example of a hold marketing and the VALORECLIN LOGO.
VALORECLIN have 5 clinics and we are serious whit lot of doctors. We are doing lot of medical service. I put a doctor picture, but if you have a better choice for the presentation folder don't hesitate to use it.

Target Market(s)

Medical customer and corporation

Industry/Entity Type

Health care

Requirements
Must have
• Professional design - red accent
Nice to have
• Medical doctor picture
Should not have
• Don't want the same hold design that the example

```html
<!DOCTYPE html>
<html lang="en">
<head>
<meta charset="utf-8">
<title>VALORECLIN Presentation Folder</title>
<link href="https://fonts.googleapis.com/css2?family=Poppins:wght@400;500;600;800&display=swap" rel="stylesheet">
<style>
  :root {
    --backdrop: #440000;
    --red: #e0202e;
    --red-deep: #c81a27;
    --ink: #000000;
    --paper: #ffffff;
    --photo-light: #f2f2f2;
    --photo-mid: #d9d6d4;
  }
  html, body { margin: 0; padding: 0; overflow: hidden; }
  body { width: 1200px; height: 1200px; background: var(--backdrop); font-family: "Poppins", sans-serif; }
  .folder { position: relative; width: 1200px; height: 1200px; }
  .folder-shapes { position: absolute; inset: 0; }
  .brand-small {
    position: absolute; left: 110px; top: 150px;
    display: flex; align-items: center; gap: 10px;
    color: var(--red); font-weight: 800; font-size: 26px; letter-spacing: 1px;
  }
  .brand-small .mark { width: 22px; height: 22px; background: var(--red); }
  .brand-main { position: absolute; left: 688px; top: 186px; color: var(--ink); font-weight: 800; font-size: 98px; line-height: 86px; letter-spacing: -2px; }
  .brand-main .line-one { display: flex; align-items: center; gap: 14px; }
  .brand-main .mark { width: 66px; height: 66px; background: var(--red); }
  .tagline {
    position: absolute; left: 688px; top: 369px; width: 471px; height: 43px;
    background: var(--ink); color: var(--paper);
    font-size: 25px; font-weight: 400; line-height: 43px; text-align: center; white-space: nowrap;
  }
  .contact-button {
    position: absolute; left: 771px; top: 523px; width: 289px; height: 56px;
    background: var(--ink); color: var(--paper); border-radius: 18px;
    font-size: 33px; font-weight: 600; line-height: 56px; text-align: center;
  }
  .contact-card {
    position: absolute; left: 702px; top: 621px; width: 427px; height: 162px;
    background: var(--paper); border-radius: 12px;
  }
  .contact-row { position: absolute; left: 24px; display: flex; align-items: flex-start; gap: 32px; color: var(--ink); }
  .contact-row svg { flex: none; }
  .contact-row.phone { top: 8px; font-size: 26px; font-weight: 500; letter-spacing: 5px; }
  .contact-row.email { top: 52px; font-size: 26px; }
  .contact-row.address { top: 96px; font-size: 19.5px; line-height: 25px; }
  .flap-brand {
    position: absolute; left: 210px; top: 960px; width: 280px;
    display: flex; align-items: center; gap: 14px;
    transform: rotate(180deg);
    color: var(--ink); font-weight: 800; font-size: 34px; letter-spacing: -0.5px;
  }
  .flap-brand .mark { width: 60px; height: 60px; background: var(--red); }
</style>
</head>
<body>
<div class="folder">
  <svg class="folder-shapes" width="1200" height="1200" viewBox="0 0 1200 1200">
    <defs>
      <linearGradient id="photoTone" x1="0" y1="0" x2="1" y2="1">
        <stop offset="0" stop-color="var(--photo-light)"/>
        <stop offset="1" stop-color="var(--photo-mid)"/>
      </linearGradient>
    </defs>
    <!-- side flap -->
    <polygon class="side-flap" points="3,594 68,590 68,840 3,810" fill="var(--paper)"/>
    <!-- bottom pocket flap -->
    <path class="pocket-flap" d="M68,845 L632,845 L610,1060 Q600,1112 545,1112 L98,1112 Q70,1112 70,1085 Z" fill="var(--paper)"/>
    <!-- main cover panel -->
    <path class="cover" d="M68,87 L1165,87 Q1195,87 1195,117 L1195,815 Q1195,845 1165,845 L68,845 Z" fill="var(--paper)"/>
    <!-- doctor photo area -->
    <rect class="photo" x="68" y="87" width="650" height="758" fill="url(#photoTone)" role="img" aria-label="Photo of a smiling doctor in a white coat with a stethoscope, writing on a clipboard"/>
    <!-- red accent bands -->
    <polygon points="702,87 1195,87 1195,165 773,165" fill="var(--red)"/>
    <polygon points="1000,87 1195,87 1195,165 1080,165" fill="var(--red-deep)" opacity="0.5"/>
    <rect x="650" y="165" width="545" height="264" fill="var(--paper)"/>
    <polygon points="845,429 1195,429 1195,845 438,845" fill="var(--red)"/>
    <polygon points="1100,490 1195,580 1195,600 1020,600" fill="var(--red-deep)" opacity="0.6"/>
    <polygon points="68,646 267,838 68,845" fill="var(--red)"/>
    <polygon points="68,668 240,838 68,838" fill="var(--red-deep)" opacity="0.5"/>
  </svg>

  <div class="brand-small"><span class="mark"></span>VALORECLIN</div>

  <div class="brand-main">
    <div class="line-one"><span class="mark"></span>VALOR</div>
    <div class="line-two">ECLIN</div>
  </div>

  <div class="tagline">LE BON CHOIX - THE RIGHT CHOICE</div>

  <div class="contact-button">CONTECT US</div>

  <div class="contact-card">
    <div class="contact-row phone">
      <svg width="32" height="32" viewBox="0 0 32 32"><circle cx="16" cy="16" r="16" fill="#000"/><path d="M11 9 L14 9 L15 13 L13 14 Q14 18 18 19 L19 17 L23 18 L23 21 Q22 23 19 23 Q10 21 9 12 Q9 9 11 9 Z" fill="#fff"/></svg>
      <span>418 555-0142</span>
    </div>
    <div class="contact-row email">
      <svg width="32" height="32" viewBox="0 0 32 32"><circle cx="16" cy="16" r="16" fill="#000"/><rect x="8" y="11" width="16" height="11" rx="1.5" fill="#fff"/><path d="M8 12 L16 18 L24 12" stroke="#000" stroke-width="1.6" fill="none"/></svg>
      <span>info@valoreclin.com</span>
    </div>
    <div class="contact-row address">
      <svg width="32" height="32" viewBox="0 0 32 32"><circle cx="16" cy="16" r="16" fill="#000"/><path d="M16 7 Q22 7 22 13 Q22 17 16 23 Q10 17 10 13 Q10 7 16 7 Z" fill="#fff"/><circle cx="16" cy="13" r="2.5" fill="#000"/><rect x="11" y="24" width="10" height="1.6" fill="#fff"/></svg>
      <span>125, rue des erables, local 310<br>Quebec(Quebec) G1A 0B2</span>
    </div>
  </div>

  <div class="flap-brand"><span class="mark"></span>VALORECLIN</div>
</div>
</body>
</html>
```